依頼詳細
◆デザインテイスト
・シンプルだが華やかなもの
・生花が入っていることが想像つくもの(配送業者に投げられないように)
・老若男女、誰が贈られても嬉しくなるデザイン
・白地のダンボールに単色カラーで印刷を予定(カラーは問わない)
※多色NG

◆デザイン種類
・「ヌベシ 1入 (80サイズ)」「ムテギ 1入 (60サイズ)」の2種ありますが、統一デザインでOKです
※成果物としては2種必要です
展開図と、花が入った状態の写真を添付させていただきます。

◆箱の仕様
・花、鉢が抜けてしまわないよう、下部に折り返しのストッパーがついています
※上部にも同様のストッパー付き

・添付の画像には「丸穴」がついておりますが、実際にはついておりません。
※展開図の通り

希望イメージ
シンプル 複雑
単色 カラフル
暗い 明るい
日常 高級
遊び心 厳粛
未来的 伝統的
女性的 男性的
希望する色
納品ファイル
• 高解像度JPG (.jpg)
• イラストレーター形式 (.ai)
補足説明
※多色NG
と記載させていただきましたが、無地の茶段ボールへの単色カラー印刷でもOKです。
■ 選んだ理由

シンプルなデザインながら、おしゃれな印象があったため。

■ 提案者全員のお礼・コメント

多くのご提案をいただきましてありがとうございます。
今後ともよろしくお願いいたします。

```html
<!DOCTYPE html>
<html lang="en">
<head>
<meta charset="utf-8">
<title>Phalaenopsis orchid — carton dieline</title>
<link rel="stylesheet" href="https://fonts.googleapis.com/css2?family=Cormorant+Garamond:wght@500&display=swap">
<style>
  :root {
    --paper: #ffffff;
    --ink-red: #d8462c;
    --die-line: #3a3a3a;
  }
  html, body {
    margin: 0;
    padding: 0;
    width: 1200px;
    height: 2168px;
    overflow: hidden;
    background: var(--paper);
  }
  .dieline {
    display: block;
    width: 1200px;
    height: 2168px;
  }
  .cut { fill: none; stroke: var(--die-line); stroke-width: 0.4; stroke-linejoin: round; }
  .fold { fill: none; stroke: var(--die-line); stroke-width: 0.4; stroke-dasharray: 2.2 1.6; }
  .badge { fill: var(--ink-red); }
  .label {
    fill: var(--ink-red);
    font-family: "Cormorant Garamond", Georgia, serif;
    font-weight: 500;
  }
  .label--small { font-size: 6.2px; }
  .label--spine { font-size: 13px; letter-spacing: 1.4px; }
</style>
</head>
<body>
<svg class="dieline" viewBox="0 0 300 542" preserveAspectRatio="none" xmlns="http://www.w3.org/2000/svg">
  <!-- glue flap -->
  <polygon class="cut" points="20,90 5,96 5,520 20,527"/>

  <!-- top flaps -->
  <path class="cut" d="M92,90 L97,70 Q99,62 107,62 L150,62 Q158,62 160,70 L165,90"/>
  <path class="cut" d="M165,90 L165,30 L237,30 L237,90"/>
  <path class="cut" d="M165,30 L172,8 Q174,2 180,2 L222,2 Q228,2 230,8 L237,30"/>
  <path class="cut" d="M237,90 L242,70 Q244,62 252,62 L285,62 Q293,62 295,70 L298,90"/>

  <!-- body outline and panel folds -->
  <rect class="cut" x="20" y="90" width="278" height="390"/>
  <line class="cut" x1="92" y1="90" x2="92" y2="480"/>
  <line class="cut" x1="165" y1="90" x2="165" y2="480"/>
  <line class="cut" x1="237" y1="90" x2="237" y2="480"/>

  <!-- top stopper slots -->
  <g class="slots">
    <rect class="cut" x="8" y="120" width="26" height="8"/>
    <rect class="cut" x="80" y="120" width="24" height="8"/>
    <rect class="cut" x="135" y="120" width="24" height="8"/>
    <rect class="cut" x="225" y="120" width="24" height="8"/>
  </g>

  <!-- bottom stopper folds -->
  <line class="fold" x1="5" y1="425" x2="298" y2="425"/>
  <line class="fold" x1="5" y1="440" x2="298" y2="440"/>
  <g class="slots">
    <rect class="cut" x="8" y="425" width="26" height="15"/>
    <rect class="cut" x="80" y="425" width="24" height="15"/>
    <rect class="cut" x="135" y="425" width="24" height="15"/>
    <rect class="cut" x="225" y="425" width="24" height="15"/>
  </g>

  <!-- bottom flaps -->
  <polyline class="cut" points="20,480 20,525 30,525 30,540 92,540 92,480"/>
  <polyline class="cut" points="92,505 105,528 105,540 152,540 152,528 165,505"/>
  <polyline class="cut" points="165,480 165,520 175,540 228,540 237,520 237,480"/>
  <line class="cut" x1="165" y1="495" x2="190" y2="520"/>
  <polyline class="cut" points="237,505 250,528 250,540 285,540 285,528 298,505 298,480"/>

  <!-- tuck flap badge -->
  <circle class="badge" cx="201" cy="18" r="11"/>

  <!-- front panels -->
  <g class="front-panel">
    <circle class="badge" cx="65" cy="245" r="22"/>
    <text class="label label--small" x="65" y="293" text-anchor="middle">Phalaenopsis</text>
    <text class="label label--small" x="65" y="305" text-anchor="middle">orchid</text>
  </g>
  <g class="front-panel">
    <circle class="badge" cx="201" cy="245" r="22"/>
    <text class="label label--small" x="201" y="293" text-anchor="middle">Phalaenopsis</text>
    <text class="label label--small" x="201" y="305" text-anchor="middle">orchid</text>
  </g>

  <!-- side panels -->
  <text class="label label--spine" transform="translate(125,175) rotate(90)" textLength="182" lengthAdjust="spacing">Phalaenopsis orchid</text>
  <text class="label label--spine" transform="translate(262,175) rotate(90)" textLength="182" lengthAdjust="spacing">Phalaenopsis orchid</text>
</svg>
</body>
</html>
```